Halt and Thicken New Branding Stationary Set - updated Oct 30th 2017

Updated on 30th Oct 2017 as we now need a whole folder design instead of a folder cover. We have thought out exactly what should be on it so it wont be hard. We are happy for this to be completed only by the winning designer if you like. And also we are guaranteeing this project now. Thanks!

We just got our new logo and now we would like a stationary set so we can brand our company communications. The items we need designed are:
Business cards
Letterhead
Appointment confirmation cards
Folder - switched from folder cover. Note that if you don't wish to do this unless you are selected as the winner this is fine.

1. Business cards - for 5 employees, final names will be given once the winner is selected, but you can use this one as the sample:
Lucinda Prieto
Hair Regrowth Expert
Halt and Thicken
7127 Marbury Ave, Suite 500
Kestrel Park CA 90877
lucinda@gavinthorpemd.example
(555) 238-9016

2. Letterhead 8.5" x 11.0" vertical
Halt and Thicken
Kestrel Park CA 90877
office@haltandthicken.example
(555) 238-9016

3. Appointment Confirmation cards - business card size
Halt and Thicken
Kestrel Park CA 90877
Appointment For:
Date:
Time:
If you are unable to make your appointment, please contact us to reschedule at:
(555) 238-9016
info@gavinthorpemd.example

*UPDATED*
4. Folder 9" x 12 " vertical with double pocket
We would like the infinity image from the logo made really big so the left side is on the back and the right side with the + sign is on the front and its takes up the maximum room on the folder.
On the front below the half logo it should say "A Biochemical Revolution..."
On the inside we would also like to have the infinity sign from the logo but faded and half on the left pocket half on the right.
On left inside pocket it should say (this will be partically written on top of the logo):
Gavin Thorpe MD
Precision Medicine
Halt and Thicken Hair
On the Right inside pocket it should say the following:
Because the Enemy of BETTER Health is Good Health
BETTER Ingredients
BETTER Recipe
BETTER Medicine
On the back below the logo on the bottom should be the contact information.
I attached a picture of our drawing of what we want for this to make it easier.

Here is our website to give you an idea of our branding: http://www.haltandthicken.example/

We are the only true cure for hair loss and need to look professional and highest quality and beyond reproach from an ethical standpoint. We are a medical clinic so this should be portrayed also.
We cured hair loss by analyzing biochemistry and rebalancing it so that the process reverses and your own hair can grow back naturally.

Business card information:

OK so here is the information for the business cards:

Lucinda Prieto
Hair Regrowth Expert
(555) 238-9016
www.haltandthicken.example

Marisol Quintero
Hair Growth Consultant
(555) 238-9016
marisol@gavinthorpemd.example
www.haltandthicken.example

Glenda Hutchins
CMO/COO
(555) 238-9016
glenda@haltandthicken.example
www.haltandthicken.example

Dr Lou Thorpe
President
(555) 238-9016
info@gavinthorpemd.example
www.haltandthicken.example

Halt and Thicken
Customer Service
(555) 238-9016
info@gavinthorpemd.example
www.haltandthicken.example

Target Market(s)

Men aged 20-24 who care about their appearance, care about their hair and care about the world.

Industry/Entity Type

Medical And Science

Font styles to use
Sans Serif

Colors
00a990
ffffff
9d9d9d
333333

Requirements
Must have
• Must use the logo and our brand colors from the logo in all designs.
• The pantone colors are:
• Green: #4ca26f
• Light Grey: #999999
• The design should be symmetrical and balanced.
Nice to have
• It should look reasonably masculine.
Should not have
• Do not include any red in the design.

```html
<!DOCTYPE html>
<html lang="en">
<head>
<meta charset="utf-8">
<title>Halt and Thicken – Stationery Set</title>
<link href="https://fonts.googleapis.com/css2?family=Montserrat:wght@400;500;600;700&display=swap" rel="stylesheet">
<style>
  :root {
    --green: #4ca26f;
    --grey: #999999;
    --dark: #555555;
    --ink: #333333;
    --backdrop: #dcdde0;
    --paper: #ffffff;
  }
  * { margin: 0; padding: 0; box-sizing: border-box; }
  html, body { width: 1200px; height: 1035px; overflow: hidden; }
  body {
    background: var(--backdrop);
    font-family: "Montserrat", sans-serif;
    color: var(--ink);
    position: relative;
  }
  .sheet {
    position: absolute;
    top: 27px;
    width: 560px;
    height: 725px;
    background: var(--paper);
    box-shadow: 0 1px 4px rgba(0,0,0,.18);
    overflow: hidden;
  }
  .sheet--letter { left: 27px; }
  .sheet--cover { left: 614px; }

  .brand {
    position: absolute;
    left: 0; right: 0;
    display: flex;
    align-items: center;
    justify-content: center;
    gap: 6px;
    color: var(--green);
    font-weight: 600;
    white-space: nowrap;
  }
  .brand__dot { border-radius: 50%; background: var(--green); flex: none; }
  .brand--letter { top: 76px; font-size: 18px; }
  .brand--letter .brand__dot { width: 14px; height: 14px; }
  .brand--cover { top: 322px; font-size: 34px; gap: 12px; }
  .brand--cover .brand__dot { width: 28px; height: 28px; }

  .cover-rule { position: absolute; height: 2px; background: var(--green); }
  .cover-rule--top { left: 216px; width: 290px; top: 380px; }
  .cover-rule--bottom { left: 54px; width: 290px; top: 440px; }
  .cover-title {
    position: absolute; left: 0; right: 0; top: 390px;
    text-align: center; font-size: 22px; font-weight: 500; color: var(--dark);
  }
  .cover-subtitle {
    position: absolute; left: 0; right: 0; top: 418px;
    text-align: center; font-size: 13px; color: var(--grey); letter-spacing: .2px;
  }

  .sheet-footer { position: absolute; left: 0; bottom: 0; width: 560px; height: 70px; }
  .sheet-footer svg { position: absolute; inset: 0; }
  .sheet-footer__name {
    position: absolute; left: 70px; top: 41px; width: 110px;
    font-size: 7px; font-weight: 700; color: #fff; text-align: right;
  }
  .sheet-footer__divider {
    position: absolute; left: 182px; top: 32px; width: 1px; height: 24px; background: #fff;
  }
  .sheet-footer__info {
    position: absolute; left: 190px; top: 34px;
    font-size: 7.2px; line-height: 11px; color: #fff; font-weight: 500; white-space: nowrap;
  }

  .card {
    position: absolute; top: 778px; width: 131px; height: 230px;
    border-radius: 8px; overflow: hidden;
    box-shadow: 0 1px 3px rgba(0,0,0,.15);
    text-align: center;
  }
  .card--light { background: var(--paper); }
  .card--green { background: var(--green); color: #fff; }
  .card--profile { left: 167px; }
  .card--profile-back { left: 316px; }
  .card--appointment { left: 754px; }
  .card--appointment-back { left: 902px; }

  .card .brand { font-size: 9.5px; gap: 4px; }
  .card .brand .brand__dot { width: 8px; height: 8px; }
  .card--light .brand { top: 48px; }
  .card--green .brand { color: #fff; }
  .card--green .brand .brand__dot { background: #fff; }
  .card--profile-back .brand { top: 112px; font-size: 10.5px; }
  .card--appointment-back .brand { top: 100px; font-size: 10.5px; }

  .card__text { position: absolute; left: 0; right: 0; font-size: 6.4px; line-height: 8px; }
  .card__name { top: 93px; font-size: 8px; font-weight: 700; color: var(--green); }
  .card__role { top: 103px; font-size: 5.6px; color: var(--grey); }
  .card__rule { position: absolute; left: 44px; width: 43px; top: 114px; height: 1px; background: var(--grey); }
  .card__contact { top: 120px; }
  .card__company { top: 166px; font-weight: 700; font-size: 5.6px; }
  .card__address { top: 174px; font-size: 5.6px; line-height: 7.5px; }

  .card__field { position: absolute; left: 9px; right: 9px; font-size: 6px; text-align: left; color: var(--dark); }
  .card__field::after {
    content: ""; position: absolute; left: 0; right: 0; top: 15px; height: 1px; background: #bbb;
  }
  .card__field--date { top: 84px; }
  .card__field--time { top: 117px; }
  .card__notice { top: 160px; font-size: 5.6px; line-height: 7.3px; color: var(--ink); }

  .card__footer { position: absolute; left: 0; bottom: 0; width: 131px; height: 32px; }
  .card__footer svg { position: absolute; inset: 0; }
  .card__web {
    position: absolute; left: 0; right: 0; top: 16px;
    font-size: 6.6px; font-weight: 700; color: #fff;
  }
  .card__back-address { bottom: 14px; font-size: 5.6px; line-height: 7.5px; font-weight: 600; }
  .card__back-address strong { font-weight: 700; }
</style>
</head>
<body>

<section class="sheet sheet--letter" aria-label="Letterhead">
  <div class="brand brand--letter"><span class="brand__dot"></span>HALT AND THICKEN</div>
  <footer class="sheet-footer">
    <svg viewBox="0 0 560 70" width="560" height="70" aria-hidden="true">
      <path d="M0 70 Q280 -66 560 70" fill="none" stroke="var(--grey)" stroke-width="3"/>
      <path d="M0 70 Q280 -52 560 70 Z" fill="var(--green)"/>
    </svg>
    <div class="sheet-footer__name">HALT AND THICKEN</div>
    <div class="sheet-footer__divider"></div>
    <div class="sheet-footer__info">
      7127 Marbury Ave, Suite 500 Kestrel Park CA 90877<br>
      office@haltandthicken.example &nbsp;•&nbsp; (555) 238-9016 &nbsp;•&nbsp; www.haltandthicken.example
    </div>
  </footer>
</section>

<section class="sheet sheet--cover" aria-label="Report cover">
  <div class="brand brand--cover"><span class="brand__dot"></span>HALT AND THICKEN</div>
  <div class="cover-rule cover-rule--top"></div>
  <h1 class="cover-title">Title Lorem Ipsum Dolor Amet Consecte</h1>
  <p class="cover-subtitle">Subtitle donec blanditg enim vitaenis verra rutrum biendum</p>
  <div class="cover-rule cover-rule--bottom"></div>
  <footer class="sheet-footer">
    <svg viewBox="0 0 560 70" width="560" height="70" aria-hidden="true">
      <path d="M0 70 Q280 -66 560 70" fill="none" stroke="var(--grey)" stroke-width="3"/>
      <path d="M0 70 Q280 -52 560 70 Z" fill="var(--green)"/>
    </svg>
    <div class="sheet-footer__name">HALT AND THICKEN</div>
    <div class="sheet-footer__divider"></div>
    <div class="sheet-footer__info">
      7127 Marbury Ave, Suite 500 Kestrel Park CA 90877<br>
      office@haltandthicken.example &nbsp;•&nbsp; (555) 238-9016 &nbsp;•&nbsp; www.haltandthicken.example
    </div>
  </footer>
</section>

<article class="card card--light card--profile" aria-label="Business card front">
  <div class="brand"><span class="brand__dot"></span>HALT AND THICKEN</div>
  <p class="card__text card__name">LUCINDA PRIETO</p>
  <p class="card__text card__role">Hair Regrowth Expert</p>
  <div class="card__rule"></div>
  <p class="card__text card__contact">lucinda@gavinthorpemd.example<br>(555) 238-9016</p>
  <p class="card__text card__company">HALT AND THICKEN</p>
  <p class="card__text card__address">7127 Marbury Ave, Suite 500<br>Kestrel Park CA 90877</p>
  <footer class="card__footer">
    <svg viewBox="0 0 131 32" width="131" height="32" aria-hidden="true">
      <path d="M0 18 Q65.5 -6 131 18" fill="none" stroke="var(--grey)" stroke-width="2"/>
      <path d="M0 22 Q65.5 0 131 22 V32 H0 Z" fill="var(--green)"/>
    </svg>
    <p class="card__web">www.haltandthicken.example</p>
  </footer>
</article>

<article class="card card--green card--profile-back" aria-label="Business card back">
  <div class="brand"><span class="brand__dot"></span>HALT AND THICKEN</div>
</article>

<article class="card card--light card--appointment" aria-label="Appointment card front">
  <div class="brand"><span class="brand__dot"></span>HALT AND THICKEN</div>
  <p class="card__field card__field--date">DATE:</p>
  <p class="card__field card__field--time">TIME:</p>
  <p class="card__text card__notice">If you cannot make your appointment,<br>please contact us to reschedule at:<br>(555) 238-9016<br>info@gavinthorpemd.example</p>
  <footer class="card__footer">
    <svg viewBox="0 0 131 32" width="131" height="32" aria-hidden="true">
      <path d="M0 18 Q65.5 -6 131 18" fill="none" stroke="var(--grey)" stroke-width="2"/>
      <path d="M0 22 Q65.5 0 131 22 V32 H0 Z" fill="var(--green)"/>
    </svg>
    <p class="card__web">www.haltandthicken.example</p>
  </footer>
</article>

<article class="card card--green card--appointment-back" aria-label="Appointment card back">
  <div class="brand"><span class="brand__dot"></span>HALT AND THICKEN</div>
  <p class="card__text card__back-address"><strong>HALT AND THICKEN</strong><br>7127 Marbury Ave, Suite 500<br>Kestrel Park CA 90877</p>
</article>

</body>
</html>
```